distributor of aftermarket auto electrical components

I am after business card design for my new company called
Summit Vehicle Supplies (SVS as the acronym). I will supplying automotive wiring components, basically from battery to headlight. I will be aiming to sell in the 4wd scene and to auto electricians. i am not worried which colours are used though i would like it to be dynamic.
Updates

sorry guys, i have add a mobile and e-mail address that will need to on there as well. Sorry for theĀ inconvenience.

sorry guys i had erred on my spelling with my e-mail. i have now fixed it in the brief

Target Market(s)

4wd industry, custom cars, RV, auto electricians

Industry/Entity Type

Electrical

Requirements
Must have
• Company Name
ABN number: 71 306 548 290
Director: Derek Holloway
M 0432 718 946
E dhollo@fernwire.com.au

```html
<!DOCTYPE html>
<html lang="en">
<head>
<meta charset="utf-8">
<title>Summit Vehicle Supplies – Business Card</title>
<link rel="stylesheet" href="https://fonts.googleapis.com/css2?family=Cabin:wght@400;700&family=Roboto+Condensed:wght@400&display=swap">
<style>
  :root {
    --brand-blue: #2e3192;
    --brand-orange: #f7934c;
    --vehicle-tone: #8a5f84;
    --page: #ffffff;
  }
  * { margin: 0; padding: 0; box-sizing: border-box; }
  html, body {
    width: 1200px;
    height: 900px;
    overflow: hidden;
    background: var(--page);
  }
  .card {
    position: absolute;
    left: 0;
    top: 92px;
    width: 1200px;
    height: 656px;
  }
  .card-face {
    position: absolute;
    left: 0;
    top: 0;
    width: 1200px;
    height: 540px;
    background: var(--brand-blue);
  }
  .company-name {
    position: absolute;
    left: 80px;
    top: 28px;
    font-family: "Cabin", sans-serif;
    font-weight: 700;
    font-size: 134px;
    line-height: 130px;
    letter-spacing: 1px;
    text-transform: uppercase;
    color: var(--brand-orange);
  }
  .abn {
    position: absolute;
    left: 82px;
    top: 468px;
    font-family: "Roboto Condensed", sans-serif;
    font-size: 32px;
    color: var(--brand-orange);
  }
  .vehicle-art {
    position: absolute;
    left: 828px;
    top: 392px;
    width: 320px;
    height: 126px;
  }
  .contact-strip {
    position: absolute;
    left: 0;
    top: 540px;
    width: 1200px;
    height: 116px;
    background: var(--brand-orange);
    display: flex;
    align-items: center;
    padding-left: 76px;
    font-family: "Cabin", sans-serif;
    font-size: 32px;
    color: var(--brand-blue);
    white-space: nowrap;
  }
  .contact-strip .label { font-weight: 700; }
  .contact-strip .item { margin-right: 22px; }
</style>
</head>
<body>
  <div class="card">
    <div class="card-face">
      <h1 class="company-name">Summit<br>Vehicle<br>Supplies</h1>
      <p class="abn">ABN number: 71 306 548 290</p>
      <svg class="vehicle-art" viewBox="0 0 320 126" role="img" aria-label="Dotted outline illustration of a car in profile">
        <rect x="0" y="0" width="320" height="126" rx="18" fill="var(--vehicle-tone)"/>
      </svg>
    </div>
    <div class="contact-strip">
      <span class="item"><span class="label">Derek Holloway</span> Director</span>
      <span class="item"><span class="label">M:</span> 0432 718 946</span>
      <span class="item"><span class="label">E:</span> dhollo@fernwire.com.au</span>
    </div>
  </div>
</body>
</html>
```